Team 5164 Reunion and Anniversary Party!

My work team will be having a reunion party for past and present members which will also serve as a 25th company anniversary celebration for two of our leaders. We were hoping to secure a fun (yet classy) design that could be used in an email template for a mass email invitation. Thank you!

```html
<!DOCTYPE html>
<html lang="en">
<head>
<meta charset="UTF-8">
<title>Team 5164 Reunion – 25th Anniversary Party</title>
<link href="https://fonts.googleapis.com/css2?family=Great+Vibes&family=DM+Sans:wght@300;400&family=Playfair+Display:wght@700&display=swap" rel="stylesheet">
<style>
  :root {
    --bg-deep: #3a0b24;
    --bg-mid: #5a1640;
    --bg-glow: #a23d7c;
    --neon: #ffd6f0;
    --neon-glow: #ff5fc4;
    --text: #ffffff;
  }
  html, body {
    margin: 0;
    padding: 0;
    overflow: hidden;
    background: var(--bg-deep);
  }
  .invite {
    position: relative;
    width: 851px;
    height: 1200px;
    overflow: hidden;
    background: linear-gradient(120deg, var(--bg-deep) 0%, var(--bg-mid) 45%, #7a1f58 75%, var(--bg-glow) 100%);
    font-family: "DM Sans", sans-serif;
    color: var(--text);
  }
  .celebration-art {
    position: absolute;
    inset: 0;
    width: 851px;
    height: 1200px;
  }
  .title {
    position: absolute;
    font-family: "Great Vibes", cursive;
    color: var(--neon);
    text-shadow: 0 0 4px var(--neon-glow), 0 0 12px var(--neon-glow), 0 0 22px rgba(255, 95, 196, .6);
    line-height: 1;
    white-space: nowrap;
  }
  .title-team { left: 250px; top: 10px; font-size: 250px; }
  .title-number { left: 360px; top: 285px; font-size: 150px; }
  .title-reunion { left: 355px; top: 435px; font-size: 96px; }
  .centered {
    position: absolute;
    left: 0;
    width: 851px;
    text-align: center;
  }
  .lead-in {
    top: 570px;
    font-size: 21px;
    font-weight: 400;
    letter-spacing: .2px;
  }
  .headline {
    top: 622px;
    margin: 0;
    font-family: "Playfair Display", serif;
    font-weight: 700;
    font-size: 56px;
    line-height: 74px;
  }
  .date-row { top: 905px; height: 90px; }
  .date-day, .date-month {
    position: absolute;
    top: 32px;
    font-size: 31px;
    font-weight: 400;
  }
  .date-day { left: 217px; }
  .date-month { left: 568px; }
  .date-number {
    position: absolute;
    left: 396px;
    top: 0;
    font-size: 98px;
    font-weight: 300;
    line-height: 1;
  }
  .time { top: 1006px; font-size: 28px; font-weight: 400; }
  .rsvp { top: 1085px; font-size: 25px; line-height: 31px; font-weight: 400; }
</style>
</head>
<body>
<main class="invite">
  <svg class="celebration-art" viewBox="0 0 851 1200" role="img" aria-label="Illustration of cheering team members raising fists and lifting a trophy amid confetti stars">
    <defs>
      <radialGradient id="trophyGlow" cx="0.82" cy="0.5" r="0.55">
        <stop offset="0" stop-color="#c24a8f" stop-opacity=".75"/>
        <stop offset="1" stop-color="#7a1f58" stop-opacity="0"/>
      </radialGradient>
      <linearGradient id="crowdShade" x1="0" y1="0" x2="0" y2="1">
        <stop offset="0" stop-color="#2e0a1e" stop-opacity="0"/>
        <stop offset="1" stop-color="#2e0a1e" stop-opacity=".55"/>
      </linearGradient>
    </defs>
    <rect width="851" height="1200" fill="url(#trophyGlow)"/>
    <rect y="820" width="851" height="380" fill="url(#crowdShade)"/>
  </svg>

  <div class="title title-team">Team</div>
  <div class="title title-number">5164</div>
  <div class="title title-reunion">Reunion</div>

  <p class="centered lead-in" style="margin:0">JOIN US IN CELEBRATING OUR</p>
  <h1 class="centered headline">25TH<br>ANNIVERSARY<br>PARTY</h1>

  <div class="centered date-row">
    <span class="date-day">Monday</span>
    <span class="date-number">14</span>
    <span class="date-month">April</span>
  </div>
  <p class="centered time" style="margin:0">at 6:30 PM</p>
  <p class="centered rsvp" style="margin:0">RSVP to Daniel<br>Phone: 555-204-8817</p>
</main>
</body>
</html>
```